Business Card Design For Bluepine Audio

Bluepine Audio is a small pro-audio company providing rental and install services for professional sound reinforcement. Focus is gigs (any gigs) needing high quality audio; from corporate to chamber music to hard hitting rock.

Bluepine Audio
Live sound for every stage ... crisp and clear
Corin Halsey
corin@bluepineaudio.com.au
0438 562 071

We need a business card design and an "drop-off"' larger card (eg. one third A4 size: 99mm wide x 210mm high) with more details.
Updates

Please note I've had limited internet access for last few days and for the next four.  The work so far looks great .. I'll provide some individual feedback on the designs now.  Great work, many thanks, love the creativity!

Corin

Industry/Entity Type

Business

```html
<!DOCTYPE html>
<html lang="en">
<head>
<meta charset="utf-8">
<title>Bluepine Audio – Business Card</title>
<link href="https://fonts.googleapis.com/css2?family=Exo+2:wght@400;500;700;800&display=swap" rel="stylesheet">
<style>
  :root {
    --page-bg: #e7e4df;
    --card-dark: #2a2e35;
    --card-dark-edge: #1f2228;
    --brand-yellow: #f7bd1c;
    --brand-yellow-light: #fbcd3a;
    --brand-orange: #e99a12;
    --ink: #2b2f36;
  }
  * { margin: 0; padding: 0; box-sizing: border-box; }
  html, body {
    width: 1200px;
    height: 1023px;
    overflow: hidden;
    background: var(--page-bg);
  }
  .business-card {
    position: absolute;
    left: 100px;
    top: 226px;
    width: 1000px;
    height: 570px;
    border-radius: 6px;
    overflow: hidden;
    background: var(--card-dark);
    box-shadow: 0 18px 40px rgba(0,0,0,0.25);
    font-family: "Exo 2", "Segoe UI", sans-serif;
    color: var(--ink);
  }
  .card-shapes {
    position: absolute;
    inset: 0;
  }
  .brand-block {
    position: absolute;
    left: 52px;
    top: 96px;
    width: 570px;
  }
  .brand-name {
    font-size: 64px;
    font-weight: 800;
    line-height: 1;
    letter-spacing: 0.5px;
  }
  .brand-tagline {
    margin-top: 14px;
    font-size: 26px;
    font-weight: 400;
    line-height: 1.1;
    white-space: nowrap;
  }
  .contact-block {
    position: absolute;
    left: 330px;
    top: 356px;
  }
  .contact-name {
    font-size: 56px;
    font-weight: 700;
    line-height: 1;
  }
  .contact-line {
    font-size: 38px;
    font-weight: 500;
    line-height: 1.2;
    margin-top: 6px;
  }
</style>
</head>
<body>
  <div class="business-card">
    <svg class="card-shapes" width="1000" height="570" viewBox="0 0 1000 570" aria-hidden="true">
      <defs>
        <linearGradient id="yellowBand" x1="0" y1="0" x2="0" y2="1">
          <stop offset="0" stop-color="#fbcd3a"/>
          <stop offset="1" stop-color="#f7bd1c"/>
        </linearGradient>
      </defs>
      <polygon points="0,84 612,84 652,124 652,224 622,254 0,254" fill="#1f2228"/>
      <polygon points="0,70 600,70 640,110 640,210 610,240 0,240" fill="url(#yellowBand)"/>
      <polygon points="0,226 616,226 610,240 0,240" fill="#e99a12"/>
      <polygon points="238,372 278,332 1000,332 1000,570 278,570 238,540" fill="#1f2228"/>
      <polygon points="250,360 290,320 1000,320 1000,570 290,570 250,530" fill="url(#yellowBand)"/>
      <polygon points="250,360 290,320 300,320 262,360" fill="#e99a12"/>
    </svg>

    <div class="brand-block">
      <div class="brand-name">Bluepine Audio</div>
      <div class="brand-tagline">Live sound for every stage ... crisp and clear</div>
    </div>

    <div class="contact-block">
      <div class="contact-name">Corin Halsey</div>
      <div class="contact-line">corin@bluepineaudio.com.au</div>
      <div class="contact-line">0438 562 071</div>
    </div>
  </div>
</body>
</html>
```